Business Cards Design for the electrical wholesaler: clean bold dynamic :)

We need a business card design that would follow our latest brand guidelines. As an electrical wholesaler we want to bring a fresh look and feel into the industry. The design should be clean bold and dynamic. It should come alive with the renewed energy of our green colour. Our grey colour should keep things balanced and complement the notion of maturity and responsibility. We employ Lato as a corporate font however are not bound by this font and we’re open to interpretation here.

Target Market(s)

Electrical contractors

Industry/Entity Type

Business

Contact Information for Business Card

Logo
Name & Surname: Olena Dovbush
Job Title: Director of Marketing
Email: helen.dovbush@mailvane.example
Cell phone: XXX.XXX.XXXX
Address: 20917 - 87 Ave. Edmonton, AB, Canada. T6K 2R8
Business Phone: 780.555.0187
Website: www.qorvil.example

Font styles to use
Other font styles liked:
• Lato

Requirements
Must have
• Logo & website
Nice to have
• Brand elements - some of them you may find in the attached Brand Guidelines (e.g. three lines on the background signifying "W")

```html
<!DOCTYPE html>
<html lang="en">
<head>
<meta charset="utf-8">
<title>Qorvil business card set</title>
<link href="https://fonts.googleapis.com/css2?family=Lato:wght@300;400;700&family=PT+Serif&display=swap" rel="stylesheet">
<style>
  :root{
    --canvas:#9b9a9b;
    --paper:#ffffff;
    --mint:#9dd3bf;
    --mint-light:#a8dcc8;
    --olive:#8f8a35;
    --navy-deep:#0f1a2b;
    --navy:#12263d;
    --navy-blue:#0f2744;
    --ink:#0f1c2b;
    --charcoal:#222222;
    --cream:#fbf8f4;
    --gold:#c9a063;
    --rust:#a8532a;
    --green:#8cc63f;
    --text:#1d1d1d;
    --text-soft:#3a3a3a;
  }
  *{box-sizing:border-box;margin:0;padding:0}
  html,body{width:1200px;height:1200px;overflow:hidden}
  body{background:var(--canvas);position:relative;font-family:"Lato",sans-serif}

  .card{position:absolute;background:var(--paper)}
  .card--front{left:62px;width:449px;height:269px}
  .card--back{left:666px;width:462px;height:278px}

  .face{position:absolute;inset:15px;overflow:hidden;display:flex}
  .panel{position:relative;height:100%}
  .panel--brand{width:48%;display:flex;align-items:center;justify-content:center}
  .panel--info{flex:1}

  .wordmark{display:flex;align-items:center;gap:7px;font-family:"Lato",sans-serif;font-weight:400;font-size:36px;letter-spacing:-0.5px;line-height:1}
  .wordmark__dot{width:22px;height:22px;border-radius:50%;background:currentColor}

  .contact{position:absolute;color:var(--text)}
  .contact__name{font-family:"Lato",sans-serif;font-weight:400;font-size:17px;letter-spacing:0.2px}
  .contact__role{font-family:"PT Serif",serif;font-size:9.5px;letter-spacing:1.4px;color:var(--text-soft);margin-bottom:10px}
  .contact__list{list-style:none}
  .contact__item{display:flex;align-items:flex-start;gap:8px;font-size:6.5px;line-height:1.1;color:var(--text-soft);margin-bottom:7px}
  .contact__item svg{width:8px;height:8px;flex:none;fill:var(--text-soft)}

  .divider{position:absolute;left:240px;top:75px;width:2px;height:90px;background:rgba(255,255,255,.75)}

  .back{position:absolute;inset:15px;display:flex;align-items:center;justify-content:center}
  .back__frame{position:absolute;inset:10px;border:1px solid var(--gold)}
  .lockup{display:flex;flex-direction:column;align-items:flex-end;gap:4px}
  .lockup .wordmark{font-size:46px}
  .lockup .wordmark__dot{width:28px;height:28px}
  .lockup__tagline{font-size:7.5px;font-weight:700;letter-spacing:1.3px}
</style>
</head>
<body>
<svg width="0" height="0" style="position:absolute">
  <defs>
    <symbol id="icon-pin" viewBox="0 0 10 10"><path d="M5 0a3.5 3.5 0 0 0-3.5 3.5C1.5 6 5 10 5 10s3.5-4 3.5-6.5A3.5 3.5 0 0 0 5 0zm0 5a1.4 1.4 0 1 1 0-2.8A1.4 1.4 0 0 1 5 5z"/></symbol>
    <symbol id="icon-mail" viewBox="0 0 10 10"><path d="M0 4l5-3 5 3v6H0z"/></symbol>
    <symbol id="icon-mobile" viewBox="0 0 10 10"><path d="M1 1l2-1 2 3-1.3 1a5 5 0 0 0 2.3 2.3L7 5l3 2-1 2C4 9 1 6 1 1z"/></symbol>
    <symbol id="icon-phone" viewBox="0 0 10 10"><path d="M0 3c0-2 10-2 10 0v1H7V3H3v1H0zM2 5h6l1 4H1z"/></symbol>
    <symbol id="icon-web" viewBox="0 0 10 10"><path d="M5 0a5 5 0 1 0 0 10A5 5 0 0 0 5 0zm0 1c.8.8 1.3 2.2 1.4 3.5H3.6C3.7 3.2 4.2 1.8 5 1zM1 5.5h1.6c.1 1.3.5 2.4 1.1 3.2A4 4 0 0 1 1 5.5zm2.6 0h2.8C6.3 6.8 5.8 8 5 9c-.8-1-1.3-2.2-1.4-3.5zm3.8 0H9a4 4 0 0 1-2.7 3.2c.6-.8 1-1.9 1.1-3.2zM1 4.5A4 4 0 0 1 3.7 1.3c-.6.8-1 1.9-1.1 3.2zm6.4 0c-.1-1.3-.5-2.4-1.1-3.2A4 4 0 0 1 9 4.5z"/></symbol>
  </defs>
</svg>

<!-- Fronts -->
<section class="card card--front" style="top:30px">
  <div class="face" style="background:var(--mint)">
    <div class="panel--brand panel" style="width:58%;color:#fff"><div class="wordmark"><span class="wordmark__dot"></span>qorvil</div></div>
    <span class="divider"></span>
    <div class="contact" style="left:262px;top:65px">
      <p class="contact__name">OLENA DOVBUSH</p>
      <p class="contact__role">Director of Marketing</p>
      <ul class="contact__list">
        <li class="contact__item"><svg><use href="#icon-pin"/></svg>20917 - 87 Ave. Edmonton<br>AB, Canada. T6K 2R8</li>
        <li class="contact__item"><svg><use href="#icon-mail"/></svg>helen.dovbush@mailvane.example</li>
        <li class="contact__item"><svg><use href="#icon-mobile"/></svg>XXX.XXX.XXXX</li>
        <li class="contact__item"><svg><use href="#icon-phone"/></svg>780.555.0187</li>
        <li class="contact__item"><svg><use href="#icon-web"/></svg>www.qorvil.example</li>
      </ul>
    </div>
  </div>
</section>

<section class="card card--front" style="top:309px">
  <div class="face">
    <div class="panel panel--brand" style="background:var(--olive);color:#fff"><div class="wordmark"><span class="wordmark__dot"></span>qorvil</div></div>
    <div class="panel panel--info" style="background:var(--mint-light)">
      <div class="contact" style="left:56px;top:68px">
        <p class="contact__name">OLENA DOVBUSH</p>
        <p class="contact__role">Director of Marketing</p>
        <ul class="contact__list">
          <li class="contact__item"><svg><use href="#icon-pin"/></svg>20917 - 87 Ave. Edmonton<br>AB, Canada. T6K 2R8</li>
          <li class="contact__item"><svg><use href="#icon-mail"/></svg>helen.dovbush@mailvane.example</li>
          <li class="contact__item"><svg><use href="#icon-mobile"/></svg>XXX.XXX.XXXX</li>
          <li class="contact__item"><svg><use href="#icon-phone"/></svg>780.555.0187</li>
          <li class="contact__item"><svg><use href="#icon-web"/></svg>www.qorvil.example</li>
        </ul>
      </div>
    </div>
  </div>
</section>

<section class="card card--front" style="top:601px">
  <div class="face">
    <div class="panel panel--brand" style="background:var(--navy-deep);color:var(--green)"><div class="wordmark"><span class="wordmark__dot"></span>qorvil</div></div>
    <div class="panel panel--info" role="img" aria-label="Light geometric line pattern on cream" style="background:var(--cream)">
      <div class="contact" style="left:62px;top:68px">
        <p class="contact__name">OLENA DOVBUSH</p>
        <p class="contact__role">Director of Marketing</p>
        <ul class="contact__list">
          <li class="contact__item"><svg><use href="#icon-pin"/></svg>20917 - 87 Ave. Edmonton<br>AB, Canada. T6K 2R8</li>
          <li class="contact__item"><svg><use href="#icon-mail"/></svg>helen.dovbush@mailvane.example</li>
          <li class="contact__item"><svg><use href="#icon-mobile"/></svg>XXX.XXX.XXXX</li>
          <li class="contact__item"><svg><use href="#icon-phone"/></svg>780.555.0187</li>
          <li class="contact__item"><svg><use href="#icon-web"/></svg>www.qorvil.example</li>
        </ul>
      </div>
    </div>
  </div>
</section>

<section class="card card--front" style="top:889px">
  <div class="face">
    <div class="panel panel--brand" style="background:var(--navy);color:var(--gold)"><div class="wordmark"><span class="wordmark__dot"></span>qorvil</div></div>
    <div class="panel panel--info" role="img" aria-label="Light geometric line pattern on cream" style="background:var(--cream)">
      <div class="contact" style="left:62px;top:68px">
        <p class="contact__name">OLENA DOVBUSH</p>
        <p class="contact__role">Director of Marketing</p>
        <ul class="contact__list">
          <li class="contact__item"><svg><use href="#icon-pin"/></svg>20917 - 87 Ave. Edmonton<br>AB, Canada. T6K 2R8</li>
          <li class="contact__item"><svg><use href="#icon-mail"/></svg>helen.dovbush@mailvane.example</li>
          <li class="contact__item"><svg><use href="#icon-mobile"/></svg>XXX.XXX.XXXX</li>
          <li class="contact__item"><svg><use href="#icon-phone"/></svg>780.555.0187</li>
          <li class="contact__item"><svg><use href="#icon-web"/></svg>www.qorvil.example</li>
        </ul>
      </div>
    </div>
  </div>
</section>

<!-- Backs -->
<section class="card card--back" style="top:21px">
  <div class="back" style="background:linear-gradient(180deg,#1f2e55 0%,#3a3550 55%,#6b3b2e 100%);color:var(--gold)">
    <span class="back__frame"></span>
    <div class="lockup"><div class="wordmark"><span class="wordmark__dot"></span>qorvil</div><span class="lockup__tagline">ELECTRICAL WHOLESALERS</span></div>
  </div>
</section>

<section class="card card--back" style="top:310px">
  <div class="back" style="background:var(--navy-blue);color:var(--gold)">
    <span class="back__frame"></span>
    <div class="lockup"><div class="wordmark"><span class="wordmark__dot"></span>qorvil</div><span class="lockup__tagline">ELECTRICAL WHOLESALERS</span></div>
  </div>
</section>

<section class="card card--back" style="top:606px">
  <div class="back" style="background:var(--ink);color:var(--rust)">
    <span class="back__frame"></span>
    <div class="lockup"><div class="wordmark"><span class="wordmark__dot"></span>qorvil</div><span class="lockup__tagline">ELECTRICAL WHOLESALERS</span></div>
  </div>
</section>

<section class="card card--back" style="top:890px">
  <div class="back" style="background:var(--charcoal);color:var(--gold)">
    <span class="back__frame"></span>
    <div class="lockup"><div class="wordmark"><span class="wordmark__dot"></span>qorvil</div><span class="lockup__tagline">ELECTRICAL WHOLESALERS</span></div>
  </div>
</section>
</body>
</html>
```